Bright Harbor Realty

We need a good looking flyer for our real estate company to impress people who are considering to sell their homes for as low as 1.5% listing commission. Please see flyer examples for reference.
555-318-4906

```html
<!DOCTYPE html>
<html lang="en">
<head>
<meta charset="utf-8">
<title>Bright Harbor Realty – Listing Flyer</title>
<link rel="stylesheet" href="https://fonts.googleapis.com/css2?family=Lato:wght@400;700;900&family=Oswald:wght@600;700&family=Roboto:wght@400;500;700&display=swap">
<style>
:root{
  --stage:#e9e7e3;
  --paper:#ffffff;
  --panel:#efefef;
  --red:#e31d25;
  --blue:#1d4fa8;
  --navy:#173f8e;
  --ink:#1b1b1b;
  --dark:#2a2a2a;
  --photo-frame:#ffffff;
}
*{margin:0;padding:0;box-sizing:border-box}
html,body{width:1200px;height:903px;overflow:hidden;background:var(--stage)}
body{position:relative;font-family:'Lato',sans-serif;color:var(--ink)}
.page{position:absolute;top:125px;width:494px;height:700px;background:var(--paper);overflow:hidden;box-shadow:0 4px 14px rgba(0,0,0,.25)}
.page--front{left:72px}
.page--back{left:632px}
.abs{position:absolute}
.panel{position:absolute;left:0;width:100%;background:var(--panel)}
.footer-band{position:absolute;left:0;bottom:0;width:100%;height:18px;background:var(--dark);z-index:1}

.brand{display:flex;align-items:center;gap:6px;font-family:'Lato',sans-serif;font-weight:900;color:var(--navy);white-space:nowrap}
.brand__mark{width:14px;height:14px;background:var(--blue);flex:none}

.headline{font-family:'Oswald',sans-serif;font-weight:700;color:var(--red);font-size:40px;line-height:40px;letter-spacing:.5px;white-space:nowrap}
.subhead{font-family:'Roboto',sans-serif;font-weight:700;color:var(--blue);font-size:15px;line-height:17px;white-space:nowrap}
.tagline{font-family:'Roboto',sans-serif;font-size:16px;line-height:19px;color:var(--ink);white-space:nowrap}

.photo{position:absolute;border:3px solid var(--photo-frame);overflow:hidden;box-shadow:0 1px 3px rgba(0,0,0,.25)}
.photo__fill{width:100%;height:100%}
.tone-house{background:linear-gradient(180deg,#9cc2e8 0%,#d9d3b5 45%,#c9bb8c 65%,#5d8a3c 100%)}
.tone-cottage{background:linear-gradient(180deg,#6aa0d8 0%,#a9b457 50%,#6f9a3a 80%,#3f6e2a 100%)}
.tone-white{background:linear-gradient(180deg,#8fb9e4 0%,#e8e6de 45%,#c8c2b6 70%,#5b8c3a 100%)}
.tone-ranch{background:linear-gradient(180deg,#4f94e0 0%,#cfc1a8 45%,#8aa86a 70%,#4e7d2e 100%)}
.tone-town{background:linear-gradient(180deg,#b8cfe6 0%,#b9a58d 45%,#9a8a78 70%,#5a5a55 100%)}
.tone-pool{background:linear-gradient(180deg,#7fb0df 0%,#d8d0b0 40%,#3fb3d9 70%,#3c7a39 100%)}
.tone-aerial{background:linear-gradient(160deg,#3f8a2f 0%,#b98f6a 45%,#d6c4a8 60%,#4c9a36 100%)}
.tone-room{background:linear-gradient(180deg,#d9dadb 0%,#bfc2c4 55%,#8a8d90 100%)}
.tone-model{background:radial-gradient(ellipse at center,#b99a6c 0%,#cdbb9a 35%,#e4e4e4 70%)}
.tone-portrait{background:linear-gradient(180deg,#dcdcdc 0%,#6b5244 40%,#2d2d33 100%)}

.ribbon{position:absolute;top:0;right:0;width:90px;height:90px;overflow:hidden}
.ribbon span{position:absolute;top:30px;right:-38px;width:150px;transform:rotate(55deg);background:var(--red);color:#fff;font-family:'Roboto',sans-serif;font-weight:500;text-align:center;font-size:8px;padding:3px 0;box-shadow:0 1px 2px rgba(0,0,0,.3)}
.ribbon--lg{width:110px;height:110px}
.ribbon--lg span{top:38px;right:-45px;width:180px;font-size:13px;padding:4px 0}

.caption{position:absolute;text-align:center;font-size:10px;line-height:12.5px;color:var(--ink)}

.did-know{position:absolute;text-align:center;font-size:10px;line-height:13px}
.did-know__title{color:var(--blue);font-size:12.5px;margin-bottom:3px}
.did-know__cta{color:var(--blue);font-size:12.5px;margin-top:3px}
.did-know__phone{display:inline-flex;align-items:center;gap:6px;font-size:10.5px;margin-top:3px}

.agent-band{position:absolute;left:78px;top:66px;width:160px;height:45px;background:var(--navy);clip-path:polygon(0 0,82% 0,100% 100%,0 100%);color:#fff;padding:5px 0 0 40px;font-family:'Roboto',sans-serif}
.agent-band__name{font-size:10px;font-weight:500;line-height:12px}
.agent-band__role{font-size:8px;line-height:10px}
.agent-band__phone{font-size:8.5px;font-weight:700;line-height:12px;display:flex;align-items:center;gap:3px}
.rule{position:absolute;left:0;top:110px;width:100%;height:2px;background:var(--blue)}
.rate-box{position:absolute;left:284px;top:24px;width:186px;height:52px;background:var(--red);border:1px solid #fff;outline:1px solid var(--red);display:flex;align-items:center;gap:8px;padding-left:12px;color:#fff;font-family:'Roboto',sans-serif}
.rate-box__num{font-family:'Oswald',sans-serif;font-weight:600;font-size:33px;line-height:1}
.rate-box__label{font-weight:700;font-size:15px;line-height:18px}

.section-title{position:absolute;left:0;width:100%;text-align:center;font-family:'Roboto',sans-serif;font-weight:700;color:var(--red);font-size:16px}
.section-sub{position:absolute;left:0;width:100%;text-align:center;font-family:'Roboto',sans-serif;font-size:12px;color:var(--ink)}
.checklist{position:absolute;list-style:none;font-size:8px;line-height:9.5px}
.checklist li{position:absolute;display:flex;gap:5px;white-space:nowrap}
.checklist svg{flex:none;margin-top:-1px}
.exposure{position:absolute;left:0;width:100%;text-align:center;color:var(--red);font-size:10px;font-weight:700}
.feature-label{position:absolute;text-align:center;font-size:10.5px;font-weight:400;color:var(--ink)}
.play{position:absolute;left:50%;top:50%;transform:translate(-50%,-50%)}
.portrait-front{z-index:2}
</style>
</head>
<body>

<section class="page page--front">
  <div class="abs brand" style="left:32px;top:44px;font-size:15px">
    <span class="brand__mark"></span>Bright Harbor Realty
  </div>

  <div class="abs headline" style="left:280px;top:20px">JUST SOLD</div>
  <div class="abs subhead" style="right:18px;top:63px">LIST FOR 1.5 % COMMISSION</div>
  <div class="abs tagline" style="right:19px;top:81px">Still Receive Top Marketing!</div>

  <div class="panel" style="top:104px;height:494px"></div>

  <div class="photo" style="left:22px;top:109px;width:450px;height:174px">
    <div class="photo__fill tone-house" role="img" aria-label="Photo of a two-storey sold home with garage and palm trees"></div>
    <div class="ribbon ribbon--lg"><span>SAVED $3,750</span></div>
  </div>
  <div class="caption" style="left:22px;top:288px;width:450px">2480 Bayview Lane, Coral Point, FL 33410 - $250,000</div>

  <div class="photo" style="left:22px;top:308px;width:206px;height:111px">
    <div class="photo__fill tone-cottage" role="img" aria-label="Photo of a single-storey green sold home"></div>
    <div class="ribbon"><span>SAVED $4,200</span></div>
  </div>
  <div class="caption" style="left:22px;top:423px;width:206px">418 W Meadowlark Drive,<br>Palm Hollow, FL 33471 - $280,000</div>

  <div class="photo" style="left:267px;top:308px;width:205px;height:111px">
    <div class="photo__fill tone-white" role="img" aria-label="Photo of a white two-storey sold home"></div>
    <div class="ribbon"><span>SAVED $1,350</span></div>
  </div>
  <div class="caption" style="left:267px;top:423px;width:205px">7765 Juniper Circle,<br>Coral Point, FL 33410 - $335,000</div>

  <div class="photo" style="left:22px;top:457px;width:206px;height:110px">
    <div class="photo__fill tone-ranch" role="img" aria-label="Photo of a ranch-style sold home with carport"></div>
    <div class="ribbon"><span>SAVED $3,443</span></div>
  </div>
  <div class="caption" style="left:12px;top:572px;width:226px">1093 Harbor Crest Circle E<br>Sandridge Beach, FL 33440 - $229,500</div>

  <div class="photo" style="left:267px;top:457px;width:205px;height:110px">
    <div class="photo__fill tone-town" role="img" aria-label="Photo of sold townhouses with parked car"></div>
    <div class="ribbon"><span>SAVED $8,250</span></div>
  </div>
  <div class="caption" style="left:257px;top:572px;width:225px">306 S Fairway Drive<br>Lakeview, FL 33460 - $550,000</div>

  <div class="photo portrait-front" style="left:44px;top:601px;width:82px;height:91px">
    <div class="photo__fill tone-portrait" role="img" aria-label="Portrait of the broker"></div>
  </div>

  <div class="did-know" style="left:150px;top:606px;width:296px">
    <div class="did-know__title">Did You Know ?</div>
    <div>On average, our customers <b>SAVE $8,750</b> when they choose us...</div>
    <div>and they still receive top mareting, service and representation!</div>
    <div class="did-know__cta">Call Us Today and Save thousands!</div>
    <div class="did-know__phone">
      <svg width="11" height="11" viewBox="0 0 24 24"><path fill="#e31d25" d="M6.6 10.8a15.1 15.1 0 0 0 6.6 6.6l2.2-2.2c.3-.3.7-.4 1-.2 1.1.4 2.3.6 3.6.6.6 0 1 .4 1 1V20c0 .6-.4 1-1 1A17 17 0 0 1 3 4c0-.6.4-1 1-1h3.5c.6 0 1 .4 1 1 0 1.3.2 2.5.6 3.6.1.3 0 .7-.2 1z"/></svg>
      555-318-4906
    </div>
  </div>

  <div class="footer-band"></div>
</section>

<section class="page page--back">
  <div class="agent-band">
    <div class="agent-band__name">MARCUS DELANEY</div>
    <div class="agent-band__role">BROKER/ OWNER</div>
    <div class="agent-band__phone">
      <svg width="7" height="7" viewBox="0 0 24 24"><path fill="#fff" d="M6.6 10.8a15.1 15.1 0 0 0 6.6 6.6l2.2-2.2c.3-.3.7-.4 1-.2 1.1.4 2.3.6 3.6.6.6 0 1 .4 1 1V20c0 .6-.4 1-1 1A17 17 0 0 1 3 4c0-.6.4-1 1-1h3.5c.6 0 1 .4 1 1 0 1.3.2 2.5.6 3.6.1.3 0 .7-.2 1z"/></svg>
      555-240-7713
    </div>
  </div>
  <div class="abs" style="left:22px;top:18px;width:86px;height:93px">
    <div class="photo__fill tone-portrait" role="img" aria-label="Portrait of the broker in a suit"></div>
  </div>
  <div class="rule"></div>

  <div class="rate-box">
    <span class="rate-box__num">1.5%</span>
    <span class="rate-box__label">Listing<br>Commission</span>
  </div>
  <div class="abs tagline" style="left:286px;top:82px;font-size:15px">Still Receive Top Marketing!</div>

  <div class="section-title" style="top:119px">SELLING YOUR HOME?</div>
  <div class="panel" style="top:141px;height:88px"></div>
  <div class="section-sub" style="top:144px">State of the Art Marketing</div>

  <ul class="checklist" style="left:0;top:0">
    <li style="left:28px;top:170px"><svg width="9" height="9" viewBox="0 0 10 10"><rect x=".5" y=".5" width="9" height="9" fill="none" stroke="#1d4fa8"/><path d="M2 5l2 2 4-5" fill="none" stroke="#1d4fa8" stroke-width="1.3"/></svg>High Definition HDR Photography</li>
    <li style="left:28px;top:190px"><svg width="9" height="9" viewBox="0 0 10 10"><rect x=".5" y=".5" width="9" height="9" fill="none" stroke="#1d4fa8"/><path d="M2 5l2 2 4-5" fill="none" stroke="#1d4fa8" stroke-width="1.3"/></svg>Aerial Photography</li>
    <li style="left:28px;top:210px"><svg width="9" height="9" viewBox="0 0 10 10"><rect x=".5" y=".5" width="9" height="9" fill="none" stroke="#1d4fa8"/><path d="M2 5l2 2 4-5" fill="none" stroke="#1d4fa8" stroke-width="1.3"/></svg>Live Video Walk- Through of Home</li>
    <li style="left:206px;top:170px"><svg width="9" height="9" viewBox="0 0 10 10"><rect x=".5" y=".5" width="9" height="9" fill="none" stroke="#1d4fa8"/><path d="M2 5l2 2 4-5" fill="none" stroke="#1d4fa8" stroke-width="1.3"/></svg>Interactive 3D Floorplan</li>
    <li style="left:206px;top:190px"><svg width="9" height="9" viewBox="0 0 10 10"><rect x=".5" y=".5" width="9" height="9" fill="none" stroke="#1d4fa8"/><path d="M2 5l2 2 4-5" fill="none" stroke="#1d4fa8" stroke-width="1.3"/></svg>For Sale Stake Sign</li>
    <li style="left:206px;top:210px"><svg width="9" height="9" viewBox="0 0 10 10"><rect x=".5" y=".5" width="9" height="9" fill="none" stroke="#1d4fa8"/><path d="M2 5l2 2 4-5" fill="none" stroke="#1d4fa8" stroke-width="1.3"/></svg>Social Media Advertising</li>
    <li style="left:340px;top:170px"><svg width="9" height="9" viewBox="0 0 10 10"><rect x=".5" y=".5" width="9" height="9" fill="none" stroke="#1d4fa8"/><path d="M2 5l2 2 4-5" fill="none" stroke="#1d4fa8" stroke-width="1.3"/></svg><span>Promoted on All Real Estate<br>Websites</span></li>
    <li style="left:340px;top:204px"><svg width="9" height="9" viewBox="0 0 10 10"><rect x=".5" y=".5" width="9" height="9" fill="none" stroke="#1d4fa8"/><path d="M2 5l2 2 4-5" fill="none" stroke="#1d4fa8" stroke-width="1.3"/></svg><span>Listing on MLS(Multiple Listing<br>Service)</span></li>
  </ul>

  <div class="exposure" style="top:236px">We Do Everything to Maximize Your Homes Exposure!</div>

  <div class="panel" style="top:252px;height:332px"></div>

  <div class="photo" style="left:28px;top:258px;width:202px;height:132px;border-color:#cfcfcf">
    <div class="photo__fill tone-pool" role="img" aria-label="Professional photo of a backyard pool and home"></div>
  </div>
  <div class="feature-label" style="left:28px;top:398px;width:202px">Professional Photography</div>

  <div class="photo" style="left:263px;top:258px;width:201px;height:132px;border-color:#cfcfcf">
    <div class="photo__fill tone-aerial" role="img" aria-label="Aerial photo of a large tile-roof home"></div>
  </div>
  <div class="feature-label" style="left:263px;top:398px;width:201px">Aerial Photography</div>

  <div class="photo" style="left:28px;top:423px;width:202px;height:133px;border-color:#cfcfcf">
    <div class="photo__fill tone-room" role="img" aria-label="Video still of a furnished living room"></div>
    <svg class="play" width="34" height="34" viewBox="0 0 34 34"><circle cx="17" cy="17" r="16" fill="#e31d25"/><circle cx="17" cy="17" r="10" fill="#fff"/><path d="M14 11.5l8 5.5-8 5.5z" fill="#e31d25"/></svg>
  </div>
  <div class="feature-label" style="left:28px;top:564px;width:202px">3D Virtual Tour</div>

  <div class="photo" style="left:263px;top:423px;width:201px;height:133px;border-color:#cfcfcf">
    <div class="photo__fill tone-model" role="img" aria-label="3D dollhouse model of a home floorplan"></div>
  </div>
  <div class="feature-label" style="left:263px;top:564px;width:201px">Video Walk-Thru</div>

  <div class="did-know" style="left:14px;top:602px;width:296px">
    <div class="did-know__title">Did You Know ?</div>
    <div>On average, our customers <b>SAVE $8,750</b> when they choose us...</div>
    <div>and they still receive top mareting, service and representation!</div>
    <div class="did-know__cta">Call Us Today and Save thousands!</div>
    <div class="did-know__phone">
      <svg width="11" height="11" viewBox="0 0 24 24"><path fill="#e31d25" d="M6.6 10.8a15.1 15.1 0 0 0 6.6 6.6l2.2-2.2c.3-.3.7-.4 1-.2 1.1.4 2.3.6 3.6.6.6 0 1 .4 1 1V20c0 .6-.4 1-1 1A17 17 0 0 1 3 4c0-.6.4-1 1-1h3.5c.6 0 1 .4 1 1 0 1.3.2 2.5.6 3.6.1.3 0 .7-.2 1z"/></svg>
      555-318-4906
    </div>
  </div>

  <div class="abs brand" style="left:330px;top:628px;font-size:12px">
    <span class="brand__mark" style="width:11px;height:11px"></span>Bright Harbor Realty
  </div>

  <div class="footer-band"></div>
</section>

</body>
</html>
```